Home Design company focused on remodel and enhancement of kitchens and bathroorms

I already have a logo designed by ArtHarbor, I now need a design for my business cards.
The company is in the remodeling and enhancement industry for homes, focusing on kitchens and bathrooms, however, we can remodel or enhance every room in a home, an office space, etc.

The company's name is VELMOR HOME DESIGN, LLC

We'll focus on clients in the Rio Grande Valley, Texas. Primarily McAllen, Edinburg, Pharr, Mission, Brownsville and South Padre Island.

The design on the business card should transmit reliability, professionalism anda bit of upscale design.

The logo is in black and white, and would like to keep it that way.

The information that needs to be printed in the business cards is:
Company's name: Velmor Home Design
Company's Logo (attached)
My name: Noel Bramwit
Address, phone and email:
2715 N Parkline Road, Ste 348
Larkmoor, CO 80921
(720) 555 0187
nbramwit@velmordesign.example
Website: velmordesign.example

```html
<!DOCTYPE html>
<html lang="en">
<head>
<meta charset="utf-8">
<title>Velmor Home Design — Business Card</title>
<link href="https://fonts.googleapis.com/css2?family=Montserrat:wght@400;700&display=swap" rel="stylesheet">
<style>
  :root {
    --backdrop: #d6d6d6;
    --card: #303030;
    --ink: #ffffff;
    --ink-soft: #d9d9d9;
    --rule: #9a9a9a;
    --emboss: #8c8c8c;
  }
  * { margin: 0; padding: 0; box-sizing: border-box; }
  html, body {
    width: 1200px; height: 913px; overflow: hidden;
    background: var(--backdrop);
    font-family: "Montserrat", sans-serif;
  }
  .sheet {
    width: 1200px; height: 913px;
    display: flex; align-items: center; justify-content: center; gap: 40px;
  }
  .card {
    width: 540px; height: 309px;
    background: var(--card);
    position: relative;
    color: var(--ink);
  }
  /* Front */
  .card-front { display: flex; align-items: center; }
  .front-brand {
    width: 230px; display: flex; align-items: center; justify-content: center; gap: 10px;
  }
  .brand-square { width: 12px; height: 12px; background: var(--ink); flex: none; }
  .brand-name {
    font-weight: 400; font-size: 15px; letter-spacing: 4px; line-height: 1.35;
    color: var(--ink); text-transform: uppercase;
  }
  .front-divider { width: 1px; height: 200px; background: var(--rule); }
  .front-details { padding-left: 28px; }
  .person-name { font-weight: 700; font-size: 24px; letter-spacing: 0.3px; }
  .person-title { font-weight: 400; font-size: 13px; color: var(--ink-soft); margin-top: 2px; }
  .contact-list { list-style: none; margin-top: 16px; }
  .contact-item {
    display: flex; align-items: center; gap: 9px;
    font-size: 12.5px; line-height: 1.75;
  }
  .contact-icon { width: 12px; height: 12px; flex: none; fill: var(--ink); }
  .address { font-size: 12.5px; line-height: 1.5; margin-top: 14px; }
  /* Back */
  .card-back { display: flex; align-items: center; justify-content: center; }
  .back-brand { display: flex; align-items: center; gap: 18px; }
  .back-brand .brand-square { width: 22px; height: 22px; background: var(--emboss); }
  .back-brand .brand-name { font-size: 26px; letter-spacing: 8px; color: var(--emboss); }
</style>
</head>
<body>
<main class="sheet">
  <section class="card card-front">
    <div class="front-brand">
      <span class="brand-square"></span>
      <p class="brand-name">Velmor<br>Home<br>Design</p>
    </div>
    <div class="front-divider"></div>
    <div class="front-details">
      <h1 class="person-name">Noel Bramwit</h1>
      <p class="person-title">Managing Director</p>
      <ul class="contact-list">
        <li class="contact-item">
          <svg class="contact-icon" viewBox="0 0 24 24"><path d="M6.6 10.8a15 15 0 0 0 6.6 6.6l2.2-2.2a1 1 0 0 1 1-.25 11.4 11.4 0 0 0 3.6.57 1 1 0 0 1 1 1V20a1 1 0 0 1-1 1A17 17 0 0 1 3 4a1 1 0 0 1 1-1h3.5a1 1 0 0 1 1 1c0 1.25.2 2.450.57 3.57a1 1 0 0 1-.25 1z"/></svg>
          (720) 555 0187
        </li>
        <li class="contact-item">
          <svg class="contact-icon" viewBox="0 0 24 24"><path d="M2 5h20v14H2z M2 5l10 8 10-8" fill="none" stroke="#fff" stroke-width="2"/></svg>
          nbramwit@velmordesign.example
        </li>
        <li class="contact-item">
          <svg class="contact-icon" viewBox="0 0 24 24"><circle cx="12" cy="12" r="9" fill="none" stroke="#fff" stroke-width="2"/><path d="M3 12h18M12 3c3 3 3 15 0 18M12 3c-3 3-3 15 0 18" fill="none" stroke="#fff" stroke-width="1.6"/></svg>
          www.velmordesign.example
        </li>
      </ul>
      <p class="address">2715 N Parkline Road,<br>Ste 348 Larkmoor, CO 80921</p>
    </div>
  </section>

  <section class="card card-back">
    <div class="back-brand">
      <span class="brand-square"></span>
      <p class="brand-name">Velmor<br>Home<br>Design</p>
    </div>
  </section>
</main>
</body>
</html>
```